TLR Property - Business Cards

Looking for a business card & general letterhead, signage etc design for our new logo.

Colours:
000a20
0056a2
00b5ef
0088ce
68cef2

Fonts:
Poppins
Karla

Please keep look and feel of new brand - example in the zip package I sent.

```html
<!DOCTYPE html>
<html lang="en">
<head>
<meta charset="utf-8">
<title>TLR Property – Business Cards</title>
<link href="https://fonts.googleapis.com/css2?family=Poppins:wght@400;600;700&family=Karla:wght@400;500&display=swap" rel="stylesheet">
<style>
  :root {
    --ink: #000a20;
    --brand-blue: #0056a2;
    --brand-cyan: #00b5ef;
    --brand-mid: #0088ce;
    --brand-light: #68cef2;
    --paper: #ffffff;
    --text-grey: #6b6f75;
    --rule-grey: #8a8d91;
    --stage: #1b1d21;
  }
  * { margin: 0; padding: 0; box-sizing: border-box; }
  html, body { width: 1200px; height: 963px; overflow: hidden; background: var(--stage); }
  .sheet {
    width: 1200px; height: 963px;
    display: flex; flex-direction: column; align-items: center; justify-content: center; gap: 36px;
  }
  .card {
    position: relative; width: 740px; height: 423px; border-radius: 24px; overflow: hidden;
    box-shadow: 0 14px 30px rgba(0,0,0,.45);
  }
  /* Front */
  .card-front { background: var(--paper); font-family: "Karla", sans-serif; }
  .holder { position: absolute; left: 52px; top: 62px; }
  .holder-name {
    font-family: "Poppins", sans-serif; font-weight: 700; font-size: 25px;
    color: var(--brand-cyan); letter-spacing: .5px; text-transform: uppercase; line-height: 1.1;
  }
  .holder-role { font-size: 19px; color: var(--text-grey); margin-top: 2px; }
  .divider { position: absolute; left: 52px; right: 150px; top: 132px; height: 1.5px; background: var(--rule-grey); }
  .contacts { position: absolute; left: 52px; top: 152px; list-style: none; }
  .contacts li { display: flex; align-items: center; gap: 12px; font-size: 19px; color: var(--text-grey); line-height: 30px; }
  .contacts svg { width: 17px; height: 17px; flex: none; }
  .front-wordmark {
    position: absolute; right: 70px; top: 160px; display: flex; align-items: center; gap: 12px;
    font-family: "Poppins", sans-serif; font-weight: 700; font-size: 40px; color: var(--brand-blue);
  }
  .front-wordmark .dot { width: 20px; height: 20px; border-radius: 50%; background: var(--brand-blue); }
  .address {
    position: absolute; right: 80px; bottom: 64px; text-align: right;
    font-size: 19px; color: var(--text-grey); line-height: 1.3;
  }
  .edge-band { position: absolute; left: 0; bottom: 0; width: 100%; height: 16px; }
  /* Back */
  .card-back {
    background:
      radial-gradient(ellipse 60% 90% at 20% 45%, rgba(104,206,242,.16), transparent 70%),
      radial-gradient(ellipse 80% 110% at 45% 40%, rgba(0,136,206,.22), transparent 70%),
      linear-gradient(135deg, #0a5db0 0%, var(--brand-blue) 55%, #0a4f98 100%);
    display: flex; align-items: center; justify-content: center;
  }
  .back-wordmark {
    display: flex; align-items: center; gap: 18px;
    font-family: "Poppins", sans-serif; font-weight: 700; font-size: 66px; color: var(--paper);
  }
  .back-wordmark .dot { width: 32px; height: 32px; border-radius: 50%; background: var(--paper); }
</style>
</head>
<body>
<main class="sheet">
  <section class="card card-front" aria-label="Business card front">
    <div class="holder">
      <p class="holder-name">Daniel Hart</p>
      <p class="holder-role">Manager</p>
    </div>
    <div class="divider"></div>
    <ul class="contacts">
      <li>
        <svg viewBox="0 0 24 24" aria-hidden="true"><path fill="#00b5ef" d="M6.6 10.8a15 15 0 0 0 6.6 6.6l2.2-2.2c.3-.3.7-.4 1-.2 1.1.4 2.3.6 3.6.6.6 0 1 .4 1 1V20c0 .6-.4 1-1 1A17 17 0 0 1 3 4c0-.6.4-1 1-1h3.5c.6 0 1 .4 1 1 0 1.3.2 2.5.6 3.6.1.3 0 .7-.2 1z"/></svg>
        555-318-2046
      </li>
      <li>
        <svg viewBox="0 0 24 24" aria-hidden="true"><rect x="2.5" y="5" width="19" height="14" rx="1.5" fill="none" stroke="#00b5ef" stroke-width="2"/><path d="M3 6l9 7 9-7" fill="none" stroke="#00b5ef" stroke-width="2"/></svg>
        hello@tlrproperty.com
      </li>
      <li>
        <svg viewBox="0 0 24 24" aria-hidden="true"><circle cx="12" cy="12" r="9.5" fill="none" stroke="#00b5ef" stroke-width="2"/><ellipse cx="12" cy="12" rx="4" ry="9.5" fill="none" stroke="#00b5ef" stroke-width="1.6"/><path d="M2.5 12h19M4 7.5h16M4 16.5h16" stroke="#00b5ef" stroke-width="1.6"/></svg>
        www.tlrproperty.com
      </li>
    </ul>
    <div class="front-wordmark"><span class="dot"></span>TLR Property</div>
    <p class="address">Your Address, City<br>State, Zip 0000</p>
    <svg class="edge-band" viewBox="0 0 740 16" preserveAspectRatio="none" aria-hidden="true">
      <polygon points="0,0 360,0 352,16 0,16" fill="var(--brand-blue)"/>
      <polygon points="366,0 740,0 740,16 358,16" fill="var(--brand-cyan)"/>
    </svg>
  </section>

  <section class="card card-back" aria-label="Business card back">
    <div class="back-wordmark"><span class="dot"></span>TLR Property</div>
  </section>
</main>
</body>
</html>
```